electrical contractor business card for professional modern company

I need a business card design for an electrical contractors business. I do all kinds of electricical work from new homes, air conditioning, data and communications. I have a logo design i want on it and have a good idea in my head of what i want it to look like. I like simple yet bold and professional looking. All black background is a must

Target Market(s)

Anyone needing electrical work done

Industry/Entity Type

Electrical

Contact Information for Business Card

company name- KPR Electrical and Data
person name-brian holloway
phone number- 0491 358 207
website-kprelec.com.au

Font styles to use
Sans Serif

Requirements
Must have
• email
• website
• logo
• name
• phone number
• list of work i do:
• -electrical
• -air-conditioning
• -data/communications
• -cctv/security
• -domestic/commercial/industrial
• -24hr emergency breakdown repair
Nice to have
• i would like the logo on the front side in the centre taking up most of the card with black background.
• on the rear i want the list of work i do with company info i.e. email, website, my name, phone number. rear of card also black background with orange writing to match the orange in the logo

```html
<!DOCTYPE html>
<html lang="en">
<head>
<meta charset="utf-8">
<title>KPR Electrical and Data — Business Card</title>
<link rel="stylesheet" href="https://fonts.googleapis.com/css2?family=Open+Sans:wght@400;600;700&display=swap">
<style>
  :root {
    --orange: #e8580f;
    --orange-deep: #d94e0a;
    --card-black: #111111;
    --ink: #141414;
    --white: #ffffff;
    --soft-white: #e6e6e6;
    --backdrop: #a9a9a9;
  }
  * { box-sizing: border-box; margin: 0; padding: 0; }
  html, body { width: 1200px; height: 720px; overflow: hidden; }
  body {
    background: var(--backdrop);
    font-family: "Open Sans", sans-serif;
    color: var(--white);
    position: relative;
  }
  .card {
    position: absolute;
    top: 189px;
    width: 560px;
    height: 342px;
    background: var(--card-black);
    overflow: hidden;
    box-shadow: 0 6px 18px rgba(0,0,0,.3);
  }
  .card--front { left: 27px; }
  .card--back { left: 613px; }

  .card__shapes { position: absolute; inset: 0; width: 100%; height: 100%; }

  .wordmark {
    position: absolute;
    font-weight: 700;
    color: var(--white);
    line-height: 1.08;
    letter-spacing: .5px;
  }
  .wordmark__dot {
    display: inline-block;
    width: 14px; height: 14px;
    border-radius: 50%;
    background: var(--orange);
    margin-right: 8px;
    vertical-align: middle;
  }

  /* Front */
  .holder { position: absolute; left: 40px; top: 38px; }
  .holder__name { color: var(--orange); font-weight: 700; font-size: 20px; }
  .holder__title { font-size: 13px; margin-top: 1px; color: var(--soft-white); }
  .card--front .wordmark { right: 36px; top: 84px; font-size: 30px; text-align: right; width: 260px; }
  .contact { position: absolute; left: 40px; top: 178px; font-size: 17px; color: var(--ink); }
  .contact__row { display: flex; align-items: center; gap: 10px; margin-bottom: 6px; }
  .contact__row svg { width: 16px; height: 16px; }
  .web { position: absolute; right: 36px; bottom: 22px; color: var(--white); font-size: 17px; display: flex; align-items: center; gap: 10px; }
  .web svg { width: 16px; height: 16px; }

  /* Back */
  .emergency {
    position: absolute; left: 0; top: 0;
    width: 250px; height: 98px;
    background: var(--orange);
    color: var(--white);
    padding: 10px 0 0 26px;
  }
  .emergency__hours { font-size: 34px; font-weight: 700; line-height: 1; }
  .emergency__label { font-size: 11.5px; font-weight: 600; letter-spacing: .3px; margin-top: 4px; }
  .card--back .wordmark { right: 36px; top: 34px; font-size: 26px; text-align: right; width: 240px; }
  .services { position: absolute; left: 40px; top: 150px; font-size: 17px; line-height: 1.6; color: var(--orange); font-weight: 600; }
  .accent-square { position: absolute; right: 0; top: 230px; width: 60px; height: 68px; background: var(--orange-deep); }
</style>
</head>
<body>

<section class="card card--front" aria-label="Card front">
  <svg class="card__shapes" viewBox="0 0 560 342" aria-hidden="true">
    <polygon points="0,150 300,150 230,342 0,342" fill="var(--orange)"/>
    <polygon points="300,150 300,250 560,250 560,342 230,342" fill="var(--orange-deep)"/>
    <line x1="275" y1="215" x2="248" y2="300" stroke="var(--white)" stroke-width="1.5" opacity=".7"/>
  </svg>

  <div class="holder">
    <p class="holder__name">Brian Holloway</p>
    <p class="holder__title">Chief Executive</p>
  </div>

  <p class="wordmark"><span class="wordmark__dot"></span>KPR Electrical and Data</p>

  <div class="contact">
    <p class="contact__row">
      <svg viewBox="0 0 16 16" aria-hidden="true"><path d="M3 1l3 3-1.5 2a9 9 0 0 0 5.5 5.5L12 10l3 3-2 2C7 15 1 9 1 3z" fill="var(--ink)"/></svg>
      0491 358 207
    </p>
    <p class="contact__row">
      <svg viewBox="0 0 16 16" aria-hidden="true"><rect x="1" y="3" width="14" height="10" fill="var(--ink)"/><path d="M1 3l7 6 7-6" stroke="var(--orange)" stroke-width="1.2" fill="none"/></svg>
      info@kprelec.com.au
    </p>
  </div>

  <p class="web">
    <svg viewBox="0 0 16 16" aria-hidden="true"><g fill="none" stroke="var(--white)" stroke-width="1.2"><circle cx="8" cy="8" r="6.5"/><ellipse cx="8" cy="8" rx="3" ry="6.5"/><path d="M1.5 8h13"/></g></svg>
    www.kprelec.com.au
  </p>
</section>

<section class="card card--back" aria-label="Card back">
  <div class="emergency">
    <p class="emergency__hours">24hr</p>
    <p class="emergency__label">EMERGENCY BREAKDOWN REPAIR</p>
  </div>

  <p class="wordmark"><span class="wordmark__dot"></span>KPR Electrical and Data</p>

  <p class="services">
    Electrical, Air-conditioning, Data/communication<br>
    Cctv/security, Domestic/commercial/industrial
  </p>

  <div class="accent-square"></div>
</section>

</body>
</html>
```